Building Company Business Card Design

I am looking to get a business card designed for my Building Company. Please find the logo attached.

Industry/Entity Type

Business

Contact Information for Business Card

Mobile 0472 913 046
Email admin@tarrowconstructworks.com.au
Website www.tarrowconstructworks.com.au

Colors
0255a3

```html
<!DOCTYPE html>
<html lang="en">
<head>
<meta charset="UTF-8">
<title>Tarrow Construct Works – Business Card</title>
<link href="https://fonts.googleapis.com/css2?family=Open+Sans:wght@400;600;700&display=swap" rel="stylesheet">
<style>
  :root {
    --brand-blue: #0255a3;
    --band-grey: #6b6d71;
    --card-dark: #2f3134;
    --card-dark-glow: #55575b;
    --card-white: #ffffff;
    --text-grey: #4a4b4e;
    --page-bg: #e9e9ea;
  }
  * { box-sizing: border-box; margin: 0; padding: 0; }
  html, body {
    width: 1200px; height: 1200px; overflow: hidden;
    background: var(--page-bg);
    font-family: "Open Sans", Arial, sans-serif;
  }
  .sheet {
    width: 1200px; height: 1200px;
    display: flex; flex-direction: column;
    align-items: center; justify-content: center; gap: 60px;
  }
  .card {
    width: 840px; height: 480px; position: relative; overflow: hidden;
    box-shadow: 0 6px 18px rgba(0,0,0,0.18);
  }
  /* Front */
  .card--front {
    background: radial-gradient(ellipse at 50% 45%, var(--card-dark-glow) 0%, var(--card-dark) 70%);
    display: flex; align-items: center; justify-content: center;
  }
  .wordmark {
    font-weight: 700; letter-spacing: 2px; text-transform: uppercase;
    display: flex; align-items: center; gap: 14px;
  }
  .wordmark__dot { width: 14px; height: 14px; border-radius: 50%; }
  .card--front .wordmark { color: #ffffff; font-size: 46px; }
  .card--front .wordmark__dot { background: #ffffff; }
  /* Back */
  .card--back { background: var(--card-white); }
  .contact { position: absolute; left: 60px; top: 60px; }
  .contact__name {
    color: var(--brand-blue); font-weight: 700; font-size: 34px;
    text-transform: uppercase; letter-spacing: -0.5px; line-height: 1.1;
  }
  .contact__role { color: var(--text-grey); font-size: 22px; margin-bottom: 14px; }
  .contact__line {
    display: flex; align-items: center; gap: 14px;
    color: var(--text-grey); font-size: 22px; line-height: 1.6;
  }
  .contact__icon { width: 20px; height: 20px; flex: none; }
  .card--back .wordmark {
    position: absolute; right: 50px; bottom: 118px;
    color: var(--brand-blue); font-size: 34px;
  }
  .card--back .wordmark__dot { background: var(--brand-blue); width: 12px; height: 12px; }
  .band {
    position: absolute; left: 0; right: 0; bottom: 22px; height: 70px;
    background: var(--band-grey);
    display: flex; align-items: center; justify-content: flex-end; padding-right: 40px;
  }
  .band__web { color: #ffffff; font-size: 20px; }
  .stripe {
    position: absolute; left: 0; right: 0; bottom: 0; height: 22px;
    background: var(--brand-blue);
  }
</style>
</head>
<body>
<main class="sheet">
  <section class="card card--front">
    <div class="wordmark"><span class="wordmark__dot"></span>Tarrow Construct Works</div>
  </section>

  <section class="card card--back">
    <div class="contact">
      <p class="contact__name">Liam Carter</p>
      <p class="contact__role">Director</p>
      <p class="contact__line">
        <svg class="contact__icon" viewBox="0 0 24 24" aria-hidden="true">
          <path fill="#0255a3" d="M6.6 10.8a15.1 15.1 0 0 0 6.6 6.6l2.2-2.2c.3-.3.7-.4 1-.2 1.1.4 2.3.6 3.6.6.6 0 1 .4 1 1V20c0 .6-.4 1-1 1A17 17 0 0 1 3 4c0-.6.4-1 1-1h3.5c.6 0 1 .4 1 1 0 1.3.2 2.5.6 3.6.1.3 0 .7-.2 1z"/>
        </svg>
        0472 913 046
      </p>
      <p class="contact__line">
        <svg class="contact__icon" viewBox="0 0 24 24" aria-hidden="true">
          <rect x="2" y="4" width="20" height="16" rx="1" fill="#0255a3"/>
        </svg>
        admin@tarrowconstructworks.com.au
      </p>
    </div>

    <div class="wordmark"><span class="wordmark__dot"></span>Tarrow Construct Works</div>

    <div class="band"><span class="band__web">www.tarrowconstructworks.com.au</span></div>
    <div class="stripe"></div>
  </section>
</main>
</body>
</html>
```